Ashcombe Field Surveyors Business Card

We are a land surveying company looking for a business card with a clean, sharp design. We would like for our design to portray our logo on one side, and contact information on the other w/ or w/o logo. Our colors preferred are navy blue, grey/silver, white and black. thank you!

Industry/Entity Type

Surveyor

Contact Information for Business Card

Ashcombe Field Surveyors
Dorian Kavatsky, P.L.S.
(555) 302-4619
Ashcombefieldsurveyors@ashmail-example.net
Ashcombefieldsurveyors-example.com
287 Linden Terrace, Brackenford 01999

Requirements
Must have
• 1. Company Name
2. Personal name and title
3. phone number
4. email.
5. website
6. address

```html
<!DOCTYPE html>
<html lang="en">
<head>
<meta charset="utf-8">
<title>Ashcombe Field Surveyors – Business Card</title>
<link href="https://fonts.googleapis.com/css2?family=Barlow:wght@400;600&display=swap" rel="stylesheet">
<style>
  :root {
    --canvas: #6f9896;
    --card-blue: #3a58dc;
    --card-white: #f3f5f4;
    --silver: #a9adb0;
    --text-white: #ffffff;
    --shadow: rgba(20, 40, 45, 0.35);
  }
  * { box-sizing: border-box; margin: 0; padding: 0; }
  html, body {
    width: 1200px; height: 1200px; overflow: hidden;
    background: var(--canvas);
    font-family: "Barlow", "Helvetica Neue", Arial, sans-serif;
  }
  .stage {
    position: relative; width: 1200px; height: 1200px;
    display: flex; flex-direction: column; align-items: center; justify-content: center; gap: 70px;
  }
  .card {
    position: relative; width: 630px; height: 360px;
    border-radius: 26px; overflow: hidden;
    box-shadow: 0 18px 40px var(--shadow);
  }

  /* Logo side */
  .card--brand { background: var(--card-blue); }
  .brand-seal {
    position: absolute; right: 34px; top: 50px;
    width: 230px; height: 230px; border-radius: 50%;
    background: var(--card-white);
    box-shadow: 0 0 0 7px var(--card-blue), 0 0 0 10px var(--silver);
    display: flex; align-items: center; justify-content: center; text-align: center;
  }
  .brand-name {
    color: var(--card-blue); font-weight: 600; font-size: 25px;
    line-height: 1.1; letter-spacing: 2px; text-transform: uppercase;
  }
  .brand-web {
    position: absolute; right: 30px; bottom: 36px;
    color: var(--text-white); font-size: 15px; font-weight: 400;
  }

  /* Contact side */
  .card--contact { background: var(--card-blue); }
  .contact-top {
    position: absolute; left: 0; top: 0; width: 100%; height: 150px;
    background: var(--card-white);
    border-bottom: 9px solid var(--silver);
  }
  .contact-logo {
    position: absolute; right: 34px; top: 40px;
    display: flex; align-items: center; gap: 12px;
  }
  .contact-logo .dot { width: 18px; height: 18px; border-radius: 50%; background: var(--card-blue); }
  .contact-logo .brand-name { font-size: 26px; }
  .contact-info {
    position: absolute; left: 40px; top: 190px; color: var(--text-white);
  }
  .company { font-size: 24px; font-weight: 400; }
  .person { font-size: 22px; font-weight: 600; margin-bottom: 20px; }
  .details { display: grid; grid-template-columns: auto auto; gap: 8px 26px; font-size: 14px; }
  .detail { display: flex; align-items: center; gap: 7px; white-space: nowrap; }
  .detail svg { width: 13px; height: 13px; flex: none; }
  .detail--address { grid-column: 1 / 3; }
</style>
</head>
<body>
<main class="stage">

  <section class="card card--brand" aria-label="Business card, logo side">
    <div class="brand-seal">
      <span class="brand-name">Ashcombe<br>Field<br>Surveyors</span>
    </div>
    <span class="brand-web">Ashcombefieldsurveyors-example.com</span>
  </section>

  <section class="card card--contact" aria-label="Business card, contact side">
    <div class="contact-top">
      <div class="contact-logo">
        <span class="dot"></span>
        <span class="brand-name">Ashcombe Field Surveyors</span>
      </div>
    </div>
    <div class="contact-info">
      <p class="company">Ashcombe Field Surveyors</p>
      <p class="person">Dorian Kavatsky, P.L.S.</p>
      <div class="details">
        <span class="detail">
          <svg viewBox="0 0 16 16" aria-hidden="true"><path fill="none" stroke="#fff" stroke-width="1.6" d="M4 2l2.5 3-1.5 1.5c1 2 2.5 3.5 4.5 4.5L11 9.5l3 2.5-1.5 2C7 13.5 2.5 9 2 3.5z"/></svg>
          (555) 302-4619
        </span>
        <span class="detail">
          <svg viewBox="0 0 16 16" aria-hidden="true"><rect x="1.5" y="3.5" width="13" height="9" rx="1" fill="none" stroke="#fff" stroke-width="1.5"/><path d="M2 4l6 5 6-5" fill="none" stroke="#fff" stroke-width="1.5"/></svg>
          Ashcombefieldsurveyors@ashmail-example.net
        </span>
        <span class="detail detail--address">
          <svg viewBox="0 0 16 16" aria-hidden="true"><path fill="#fff" d="M8 1a5 5 0 0 0-5 5c0 4 5 9 5 9s5-5 5-9a5 5 0 0 0-5-5zm0 7a2 2 0 1 1 0-4 2 2 0 0 1 0 4z"/></svg>
          287 Linden Terrace, Brackenford 01999
        </span>
      </div>
    </div>
  </section>

</main>
</body>
</html>
```